Brochure for medical doctor

I need a brochure for a medical doctor to promote his practice. The brochure should contain his picture, business information (use letterhead from attachment), and the following text:

- Now accepting PI cases on lien!
- Same and next business day appointments available for initial visits, pre-operative clearances, and all other medical needs

- Expedited medical reports sent quickly to your office

Medical

```html
<!DOCTYPE html>
<html lang="en">
<head>
<meta charset="utf-8">
<title>Northbrook Clinic – Flyer</title>
<link href="https://fonts.googleapis.com/css2?family=Oswald:wght@400&family=Montserrat:wght@500;600;700&family=Open+Sans:wght@400&display=swap" rel="stylesheet">
<style>
  :root {
    --brand-blue: #1f6fc0;
    --band-blue: #1e78c8;
    --band-light: #3a9be0;
    --ink: #1b1b1b;
    --body-ink: #262626;
    --paper: #ffffff;
    --backdrop: #7a7a7a;
    --haze-1: #e9f3f8;
    --haze-2: #b9d6e4;
    --coat-1: #e6edf3;
    --coat-2: #9fb4c6;
  }
  * { box-sizing: border-box; margin: 0; padding: 0; }
  html, body {
    width: 1200px; height: 1200px; overflow: hidden;
    background: var(--backdrop);
  }
  .flyer {
    position: absolute; left: 160px; top: 30px;
    width: 880px; height: 1140px;
    background: var(--paper);
    overflow: hidden;
    box-shadow: 0 10px 30px rgba(0,0,0,.35);
  }
  .hero-backdrop {
    position: absolute; left: 0; top: 0; width: 880px; height: 480px;
    background: linear-gradient(120deg, var(--paper) 0%, var(--haze-1) 35%, var(--haze-2) 70%, var(--haze-1) 100%);
  }
  .doctor-portrait {
    position: absolute; right: 20px; top: 10px; width: 300px; height: 470px;
    background: linear-gradient(180deg, var(--coat-1) 0%, var(--coat-2) 100%);
    border-radius: 140px 140px 0 0;
    opacity: .9;
  }
  .swoosh { position: absolute; left: 0; top: 330px; width: 880px; height: 200px; }
  .clinic-name {
    position: absolute; left: 45px; top: 58px;
    font: 700 40px/1 "Montserrat", sans-serif;
    color: var(--brand-blue);
  }
  .offer-list {
    position: absolute; left: 45px; top: 132px; width: 470px;
    list-style: none;
    font: 600 19px/1.3 "Montserrat", sans-serif; color: var(--ink);
  }
  .offer-list li { position: relative; padding-left: 34px; margin-bottom: 12px; }
  .offer-list svg { position: absolute; left: 0; top: 3px; width: 22px; height: 20px; }
  .patient-photo {
    position: absolute; left: 70px; top: 300px; width: 290px; height: 290px;
    border-radius: 50%; border: 9px solid var(--paper);
    background: radial-gradient(circle at 45% 55%, #c7cfe0 0%, #e8e3de 55%, #f3f1ee 100%);
    box-shadow: 0 2px 8px rgba(0,0,0,.18);
  }
  .lien-heading {
    position: absolute; right: 50px; top: 606px;
    font: 400 25px/1 "Oswald", sans-serif; color: var(--brand-blue);
    text-transform: uppercase;
  }
  .lien-terms {
    position: absolute; left: 45px; top: 648px; width: 790px;
    font: 400 12px/1.4 "Open Sans", sans-serif; color: var(--body-ink);
  }
  .lien-terms p { margin-bottom: 9px; }
  .blank { display: inline-block; width: 120px; border-bottom: 1px solid var(--body-ink); }
  .contact-band {
    position: absolute; left: 0; bottom: 0; width: 880px; height: 92px;
    background: var(--band-blue);
    border-top: 8px solid var(--band-light);
    display: flex; align-items: center; justify-content: space-between;
    padding: 0 45px;
    font: 500 17px/1 "Montserrat", sans-serif; color: var(--paper);
  }
  .contact-item { display: flex; align-items: center; gap: 10px; }
  .contact-item svg { width: 22px; height: 22px; }
</style>
</head>
<body>
<main class="flyer">
  <div class="hero-backdrop" role="img" aria-label="Soft blurred hospital corridor in pale blue tones"></div>
  <div class="doctor-portrait" role="img" aria-label="Portrait of a doctor in a white coat with arms crossed"></div>

  <svg class="swoosh" viewBox="0 0 880 200" preserveAspectRatio="none" aria-hidden="true">
    <path d="M0 60 C220 110 420 150 620 120 C720 105 800 80 880 55 L880 75 C790 110 700 130 600 150 C420 185 220 175 0 120 Z" fill="var(--band-blue)"/>
    <path d="M0 120 C220 175 420 185 600 150 C700 130 790 110 880 75 L880 200 L0 200 Z" fill="var(--paper)"/>
  </svg>

  <h1 class="clinic-name">Northbrook Clinic</h1>

  <ul class="offer-list">
    <li><svg viewBox="0 0 22 20" aria-hidden="true"><rect x="1" y="5" width="14" height="14" fill="none" stroke="#1b1b1b" stroke-width="2"/><path d="M4 11 L8 15 L20 2" fill="none" stroke="#1b1b1b" stroke-width="3"/></svg>Now accepting PI cases on lien !</li>
    <li><svg viewBox="0 0 22 20" aria-hidden="true"><rect x="1" y="5" width="14" height="14" fill="none" stroke="#1b1b1b" stroke-width="2"/><path d="M4 11 L8 15 L20 2" fill="none" stroke="#1b1b1b" stroke-width="3"/></svg>Same and next business day appointments available for initial visits, pre-operative clearances, and all other medical needs.</li>
    <li><svg viewBox="0 0 22 20" aria-hidden="true"><rect x="1" y="5" width="14" height="14" fill="none" stroke="#1b1b1b" stroke-width="2"/><path d="M4 11 L8 15 L20 2" fill="none" stroke="#1b1b1b" stroke-width="3"/></svg>Expedited medical reports sent quickly to your office.</li>
  </ul>

  <div class="patient-photo" role="img" aria-label="Doctor listening to an older patient's heartbeat with a stethoscope"></div>

  <h2 class="lien-heading">Medical Reports and Doctor’s Lien</h2>

  <section class="lien-terms">
    <p>I authorized the above doctor and or their authorized representatives to furnish my attorney, any attorney or attorneys who subsequently are either associated with the said attorney or substituted in their place, with a full report of my examination, diagnosis, treatment, prognosis, itemized bill of charges incurred, etc, in regard to the accident in which I was involved on <span class="blank"></span>, and hold the above doctor free and harmless from any liability in such transfer of information.</p>
    <p>Out of the proceeds of the settlement and/or judgment in my claim for personal injuries, I hereby assign, set over and transfer to the above doctor such monies due and owing to him or the group for medical, chiropractic, X-rays, physical therapy, supplies and or laboratory fees rendered to me, either by reason of the above accident or otherwise. I further give to the above doctor a lien on any and all fund received by me or in my behave in association with the settlement or satisfaction of judgement arising from claims presented on my behalf.</p>
    <p>I fully understand that I am directly responsible to said doctors/group for all medical bills submitted by them for services rendered to me. I further understand that such payment is not contingent on any settlement, judgement or verdict by which I may eventually receive said fee. In the event legal action shall be brought in order to enforce this lien, then the prevailing party shall be entitled to reasonable costs and attorney fees in addiction to any judgment rendered. It is acknowledged by the undersigned that this assignment and lien is further consideration for the services rendered by the above doctor in addition to the obligation to pay for the medical services.</p>
    <p>Patient’s personal injury claim medical payments are hereby assigned and will be paid directly from the insurance company to Northbrook Clinic.</p>
    <p>Attorney agrees to notify the doctors immediately of the name and contacting information of any attorney substituted in his or her place.</p>
  </section>

  <footer class="contact-band">
    <div class="contact-item">
      <svg viewBox="0 0 24 24" aria-hidden="true"><path d="M12 1 C6.5 1 3 5 3 9.5 C3 15 12 23 12 23 C12 23 21 15 21 9.5 C21 5 17.5 1 12 1 Z" fill="#fff"/><circle cx="12" cy="9.5" r="3.5" fill="var(--band-blue)"/></svg>
      <span>4150 Orchard Ave. Maple Grove, CA 90000</span>
    </div>
    <div class="contact-item">
      <svg viewBox="0 0 24 24" aria-hidden="true"><circle cx="12" cy="12" r="10.5" fill="none" stroke="#fff" stroke-width="2"/><path d="M8 6.5 L10 6.5 L11 9.5 L9.8 10.6 C10.5 12 11.8 13.4 13.3 14.2 L14.4 13 L17.4 14 L17.4 16 C17.4 16.7 16.8 17.3 16 17.2 C11 16.7 7.3 13 6.8 8 C6.7 7.2 7.3 6.5 8 6.5 Z" fill="#fff"/></svg>
      <span>(555) 314-2200</span>
    </div>
    <div class="contact-item">
      <svg viewBox="0 0 24 24" aria-hidden="true"><rect x="2" y="8" width="5" height="14" rx="1" fill="#fff"/><rect x="8" y="2" width="10" height="7" fill="none" stroke="#fff" stroke-width="1.6"/><rect x="8" y="8" width="14" height="14" rx="1.5" fill="#fff"/><g fill="var(--band-blue)"><rect x="10" y="11" width="2" height="2"/><rect x="14" y="11" width="2" height="2"/><rect x="18" y="11" width="2" height="2"/><rect x="10" y="15" width="2" height="2"/><rect x="14" y="15" width="2" height="2"/><rect x="18" y="15" width="2" height="2"/></g></svg>
      <span>(555) 314-2207</span>
    </div>
  </footer>
</main>
</body>
</html>
```